依頼詳細
当サイトに店舗情報等を掲載してもらうための店舗への説明用チラシのデザイン制作をお願い致します。思わず掲載をしたくなるようなデザインをお願いします。シンプルでわかり易いものが希望です。
記載項目
サイト名はsemu(セム)・店舗情報掲載料1P21,000円/年額 複数P(写真・メニュー・クーポン等)42,000円/年額 求人情報掲載無料・採用時31,500円 当サイトの収益は児童養護施設等の子供達の学習支援に使われます。
サイズ
A4
ページ数
片面
希望イメージ
シンプル 複雑
単色 カラフル
暗い 明るい
日常 高級
遊び心 厳粛
未来的 伝統的
女性的 男性的
希望する色
オレンジ
納品ファイル
• 高解像度JPG (.jpg)
• イラストレーター形式 (.ai)
補足説明
《選ぶワクワクを全ての人に》をミッションにしたNPOです。この度開設するサイトを通じて、大人の生活の選択肢を増やし、学習支援によって子どもの将来の選択肢を増やすことを目的としています。サイト開設にあたっては、一定数の店舗登録が必須なため、店舗への説明がわかりやすい営業用チラシが必要です。イメージとしてはひらけ堂やぽみたすが近いかと思います。

```html
<!DOCTYPE html>
<html lang="ja">
<head>
<meta charset="utf-8">
<title>セム 店舗掲載のご案内</title>
<link rel="stylesheet" href="https://fonts.googleapis.com/css2?family=M+PLUS+Rounded+1c:wght@500;800;900&family=Noto+Sans+JP:wght@400;700;900&display=swap">
<style>
:root{
  --orange:#f28a12;
  --orange-deep:#e86a0a;
  --orange-soft:#fbd9a8;
  --red:#e6152f;
  --green:#2f9b3a;
  --green-light:#b9dd8c;
  --blue:#1e8ad6;
  --pink:#ec5d9c;
  --purple:#9b4bb7;
  --ink:#333;
  --white:#fff;
}
*{margin:0;padding:0;box-sizing:border-box}
html,body{width:849px;height:1200px;overflow:hidden;background:var(--white)}
body{font-family:"Noto Sans JP",sans-serif;color:var(--ink)}
.flyer{position:relative;width:849px;height:1200px;overflow:hidden;background:var(--white)}
.abs{position:absolute}
ul{list-style:none}

.mission{left:0;top:0;width:849px;height:64px;background:var(--orange);color:var(--white);
  font-family:"M PLUS Rounded 1c",sans-serif;font-weight:900;font-size:44px;
  display:flex;align-items:center;justify-content:center;letter-spacing:4px;white-space:nowrap}

.tagline{left:50px;top:74px;font-family:"M PLUS Rounded 1c",sans-serif;font-weight:800;
  font-size:34px;line-height:1.2;color:var(--green);letter-spacing:2px;white-space:nowrap}
.site-name{left:50px;top:118px;height:96px;display:flex;align-items:center;gap:26px;
  font-family:"M PLUS Rounded 1c",sans-serif;font-weight:900;color:var(--orange);white-space:nowrap}
.site-name .latin{font-size:78px;letter-spacing:10px;line-height:1}
.site-name .kana{font-size:92px;line-height:1}
.site-name .dot{width:30px;height:30px;border-radius:50%;background:var(--orange)}

.photo{border-radius:4px}
.p1{left:52px;top:222px;width:252px;height:198px;background:linear-gradient(135deg,#7a4a3a,#c9a184)}
.p2{left:312px;top:222px;width:150px;height:96px;background:linear-gradient(135deg,#f3c6c9,#e9e2d6)}
.p3{left:470px;top:222px;width:160px;height:96px;background:linear-gradient(135deg,#e7ded4,#b49a7c)}
.p4{left:638px;top:222px;width:160px;height:96px;background:linear-gradient(135deg,#d4dde0,#f0f2f2)}
.p5{left:312px;top:324px;width:150px;height:96px;background:linear-gradient(135deg,#8fb96a,#dcd7a0)}
.p6{left:470px;top:324px;width:160px;height:96px;background:linear-gradient(135deg,#5a4a3e,#a8927c)}

.plate{left:618px;top:400px;width:220px;height:220px;border-radius:50%;
  background:radial-gradient(circle at 50% 50%,#d8893a 0,#c06a2a 38%,#f4efe6 60%,#e8e1d6 100%)}
.headline{left:50px;top:436px;z-index:2;font-family:"M PLUS Rounded 1c",sans-serif;font-weight:900;
  font-size:50px;line-height:1.24;color:var(--red);letter-spacing:0;white-space:nowrap;
  text-shadow:3px 3px 0 var(--white),-3px -3px 0 var(--white),3px -3px 0 var(--white),-3px 3px 0 var(--white),0 3px 0 var(--white),3px 0 0 var(--white)}

.categories{left:52px;top:586px;display:flex;gap:8px}
.cat{width:88px;height:50px;border-radius:6px;color:var(--white);text-align:center;
  font-family:"M PLUS Rounded 1c",sans-serif;font-weight:800;line-height:1.15;
  display:flex;flex-direction:column;justify-content:center;white-space:nowrap}
.cat small{font-size:12px}
.cat b{font-size:13px;letter-spacing:.3px}
.c-gourmet{background:var(--red)}
.c-beauty{background:var(--pink)}
.c-event{background:var(--green)}
.c-useful{background:var(--purple)}
.c-work{background:var(--orange)}

.label{height:30px;padding:0 14px;border-radius:4px;color:var(--white);font-weight:900;
  font-size:20px;display:flex;align-items:center;font-family:"M PLUS Rounded 1c",sans-serif;white-space:nowrap}
.label-shop{left:52px;top:648px;background:var(--red)}
.label-job{left:582px;top:648px;background:var(--blue)}

.price{top:684px;height:72px;border:3px solid var(--orange);border-radius:8px;background:var(--white);white-space:nowrap}
.price-single{left:52px;width:244px}
.price-multi{left:304px;width:266px}
.price .note{position:absolute;top:4px;left:8px;font-size:10px;line-height:1.2;color:var(--red);font-weight:700}
.price .row{position:absolute;top:20px;left:8px;display:flex;align-items:center;gap:6px}
.price .unit{background:var(--orange);color:var(--white);font-weight:900;font-size:20px;line-height:1.3;
  padding:0 6px;border-radius:4px}
.price .unit.sm{font-size:14px;padding:3px 4px}
.price .amount{font-family:"M PLUS Rounded 1c",sans-serif;font-weight:900;font-size:28px;line-height:1.1;color:var(--orange-deep)}
.price .amount small{font-size:12px;color:var(--ink);margin-left:2px}
.price .sub{position:absolute;bottom:3px;left:70px;font-size:9px;line-height:1.2;color:var(--ink)}
.job{left:582px;top:684px;width:214px;height:72px;border:3px solid var(--blue);border-radius:8px;
  display:flex;align-items:center;justify-content:center;gap:6px;background:var(--white);white-space:nowrap}
.job .when{background:var(--blue);color:var(--white);font-weight:900;font-size:15px;padding:2px 6px;border-radius:4px}
.job .amount{font-family:"M PLUS Rounded 1c",sans-serif;font-weight:900;font-size:30px;color:var(--blue)}
.job .amount small{font-size:15px}

.city{left:0;top:770px;width:849px;height:270px;
  background:linear-gradient(180deg,#ffffff 0%,#e4f3d2 40%,var(--green-light) 100%)}
.support{left:600px;top:930px;width:230px;height:86px;background:var(--white);border:2px solid var(--green);
  border-radius:6px;padding:9px 12px;font-size:14px;line-height:1.5;font-weight:700;color:var(--ink)}

.footer{left:0;top:1030px;width:849px;height:170px}
.footer-logo{left:22px;top:1090px;display:flex;align-items:center;gap:8px;padding:8px 16px;background:var(--orange);border-radius:8px;
  font-family:"M PLUS Rounded 1c",sans-serif;font-weight:900;font-size:40px;line-height:1.2;color:var(--white)}
.footer-logo .dot{width:16px;height:16px;background:var(--white);border-radius:50%}
.company{left:222px;top:1086px;color:var(--ink);white-space:nowrap}
.company .name{font-size:25px;font-weight:900;line-height:1.3}
.company .addr{font-size:14px;margin-top:6px;line-height:1.6}
.contact{left:490px;top:1078px;width:350px;text-align:center;white-space:nowrap}
.contact .ask{display:inline-block;background:var(--orange);color:var(--white);font-weight:900;font-size:19px;line-height:1.4;padding:3px 16px;border-radius:20px}
.contact .tel{font-family:"M PLUS Rounded 1c",sans-serif;font-weight:900;font-size:34px;color:var(--orange-deep);line-height:1.2;margin-top:4px}
.contact .web{font-size:16px;font-weight:700;line-height:1.4}
</style>
</head>
<body>
<main class="flyer">
  <header class="abs mission">選ぶワクワクを全ての人に</header>

  <p class="abs tagline">八代の情報ポータルサイト</p>
  <div class="abs site-name"><span class="latin">SEMU</span><span class="dot"></span><span class="kana">セム</span></div>

  <div class="abs photo p1" role="img" aria-label="化粧品やメイク道具の写真"></div>
  <div class="abs photo p2" role="img" aria-label="ショートケーキの写真"></div>
  <div class="abs photo p3" role="img" aria-label="ウェディングドレスの写真"></div>
  <div class="abs photo p4" role="img" aria-label="パソコンを使う手元の写真"></div>
  <div class="abs photo p5" role="img" aria-label="料理の写真"></div>
  <div class="abs photo p6" role="img" aria-label="お店の店内の写真"></div>

  <div class="abs plate" role="img" aria-label="グラタンスープの写真"></div>
  <h1 class="abs headline">当社のサイトに店舗情報を<br>掲載しませんか？</h1>

  <ul class="abs categories">
    <li class="cat c-gourmet"><small>ごちそう</small><b>GOURMET</b></li>
    <li class="cat c-beauty"><small>きれいになる</small><b>BEAUTIFUL</b></li>
    <li class="cat c-event"><small>たのしむ</small><b>EVENT</b></li>
    <li class="cat c-useful"><small>おやくだち</small><b>USEFULL</b></li>
    <li class="cat c-work"><small>はたらく</small><b>EORK</b></li>
  </ul>

  <div class="abs label label-shop">店舗情報掲載料</div>
  <div class="abs price price-single">
    <span class="note">お店の情報を1ページで掲載</span>
    <div class="row"><span class="unit">1P</span><span class="amount">21,000円<small>/年額</small></span></div>
  </div>
  <div class="abs price price-multi">
    <span class="note">お店の情報を複数ページで掲載</span>
    <div class="row"><span class="unit sm">複数P</span><span class="amount">42,000円<small>/年額</small></span></div>
    <span class="sub">(写真・メニュー・クーポン等)</span>
  </div>

  <div class="abs label label-job">求人情報掲載無料</div>
  <div class="abs job"><span class="when">採用時</span><span class="amount">31,500<small>円</small></span></div>

  <div class="abs city" role="img" aria-label="緑色の街並みのイラスト"></div>
  <p class="abs support">当サイトの収益は児童養護施設等の子供達の学習支援に使われます。</p>

  <svg class="abs footer" width="849" height="170" viewBox="0 0 849 170" aria-hidden="true">
    <path d="M0 30 Q424 -10 849 30 L849 170 L0 170 Z" fill="#fbd9a8"/>
    <path d="M0 40 Q424 0 849 40" fill="none" stroke="#f28a12" stroke-width="6"/>
  </svg>
  <div class="abs footer-logo"><span class="dot"></span>セム</div>
  <div class="abs company">
    <p class="name">株式会社xxxxxxx</p>
    <p class="addr">〒000-0000<br>xxxxxxxxxxxxxxx0-0-0</p>
  </div>
  <div class="abs contact">
    <p class="ask">お気軽にお問い合わせください</p>
    <p class="tel">TEL000-000-0000</p>
    <p class="web">ホームページ http://semu.co.jp</p>
  </div>
</main>
</body>
</html>
```